Flyer Design

We are a new service called chatpal.co.uk (see website) This is a premium rate £1:50 per sms text advice service. I am a qualified counsellor who already runs a practice see gavinrowecounselling.uk and have gotten per,it's ion from CALLTARIFFHUB and are registered with them for this service. Quite simply they text Q4 followed by a brief description of their personal dilemma/life or relationship concern to 64915 this is received by me and then I text back with a brief piece of guidance and feedback on their issue. So it is a text based counselling/advice service for those who want a day to day life issue dealt with in confidence,quickly and discreetly. I want the flyers to be basic with a basic and easily transferable and identifiable image like the one on my website.

Industry/Entity Type

Counsellor

```html
<!DOCTYPE html>
<html lang="en">
<head>
<meta charset="utf-8">
<title>chatpal.co.uk – Flyer</title>
<link rel="stylesheet" href="https://fonts.googleapis.com/css2?family=Luckiest+Guy&family=Open+Sans:wght@600&display=swap">
<style>
  :root {
    --backdrop: #3b2419;
    --flyer-sage: #9db0a8;
    --flyer-sage-light: #c6d3cd;
    --flyer-sage-dark: #7f958c;
    --bubble: #f7f7f5;
    --ink: #2b2b2b;
    --letter: #ffffff;
    --pale-copy: #e4ebe8;
    --skin: #f3dcb8;
    --hair: #5a5c60;
    --suit: #43474f;
    --tie: #e07f35;
    --share-tile: #d9e1dd;
  }
  * { box-sizing: border-box; margin: 0; padding: 0; }
  html, body {
    width: 1200px; height: 795px; overflow: hidden;
    background: var(--backdrop);
  }
  .canvas {
    width: 1200px; height: 795px;
    display: flex; align-items: center; justify-content: center; gap: 40px;
  }
  .flyer {
    position: relative; width: 523px; height: 740px; overflow: hidden;
    background: radial-gradient(ellipse at 60% 40%, var(--flyer-sage-light), var(--flyer-sage) 55%, var(--flyer-sage-dark));
    font-family: "Luckiest Guy", "Arial Black", sans-serif;
  }
  .outlined {
    color: var(--letter);
    -webkit-text-stroke: 1.4px var(--ink);
    paint-order: stroke fill;
    text-shadow: 2px 2px 0 rgba(0,0,0,.3);
    letter-spacing: .5px;
  }
  .site-name {
    position: absolute; top: 18px; left: 0; width: 100%;
    text-align: center; font-size: 42px; line-height: 1;
    -webkit-text-stroke: 2px var(--ink);
  }

  /* speech bubble */
  .speech-bubble {
    position: absolute; background: var(--bubble);
    border-radius: 24px; text-align: center;
  }
  .speech-bubble::after {
    content: ""; position: absolute; width: 0; height: 0;
    border-style: solid;
  }

  /* front side */
  .registration {
    position: absolute; top: 74px; right: 20px; text-align: right;
    color: var(--pale-copy);
  }
  .registration-label { font-size: 14px; letter-spacing: 1px; }
  .registration-name {
    font-family: "Open Sans", Arial, sans-serif; font-weight: 600;
    font-size: 18px; line-height: 1.1;
  }
  .front .figure {
    position: absolute; right: 0; bottom: 0; width: 230px; height: 540px;
    background: linear-gradient(180deg, var(--hair) 0 12%, var(--skin) 14% 58%, var(--suit) 64%);
    border-top-left-radius: 90px;
  }
  .front .speech-bubble {
    top: 98px; left: 20px; width: 290px;
    padding: 18px 16px 16px;
  }
  .front .speech-bubble::after {
    right: -22px; top: 250px;
    border-width: 14px 0 14px 24px;
    border-color: transparent transparent transparent var(--bubble);
  }
  .headline { font-size: 24px; line-height: 1.05; margin-bottom: 10px; }
  .topics { font-size: 19px; line-height: 1.05; margin-bottom: 12px; }
  .call-to-action { font-size: 24px; line-height: 1.05; margin-bottom: 12px; }
  .shortcode { font-size: 34px; }
  .credentials { font-size: 13px; line-height: 1.1; margin-bottom: 10px; -webkit-text-stroke: .8px var(--ink); }
  .pricing { font-size: 13px; line-height: 1.1; margin-bottom: 6px; -webkit-text-stroke: .8px var(--ink); }
  .terms { font-size: 10px; line-height: 1.1; -webkit-text-stroke: .6px var(--ink); text-shadow: none; }

  /* back side */
  .back .speech-bubble {
    top: 84px; left: 20px; width: 400px;
    padding: 18px 22px; text-align: left;
  }
  .back .speech-bubble::after {
    left: 90px; bottom: -20px;
    border-width: 22px 16px 0 0;
    border-color: var(--bubble) transparent transparent transparent;
  }
  .how-title { font-size: 16px; margin-bottom: 8px; }
  .how-step {
    font-size: 11px; line-height: 1.25; margin-bottom: 8px;
    -webkit-text-stroke: .6px var(--ink); text-shadow: none;
  }
  .how-step:last-child { margin-bottom: 0; }
  .back-notes {
    position: absolute; top: 420px; left: 24px; width: 300px;
    color: var(--pale-copy); font-size: 12px; line-height: 1.3;
    letter-spacing: .5px;
  }
  .back-notes p { margin-bottom: 10px; }
  .share-row {
    position: absolute; left: 24px; bottom: 40px; display: flex; gap: 10px;
  }
  .share-tile {
    width: 40px; height: 40px; border-radius: 8px;
    background: var(--share-tile); opacity: .8;
  }
  .back .figure {
    position: absolute; right: 0; bottom: 0; width: 170px; height: 200px;
    background: linear-gradient(180deg, var(--skin) 0 45%, var(--suit) 52%);
    border-top-left-radius: 70px;
  }
</style>
</head>
<body>
<main class="canvas">
  <article class="flyer back">
    <h2 class="site-name outlined">CHATPAL.CO.UK</h2>
    <section class="speech-bubble">
      <p class="how-title outlined">HOW IT WORKS:</p>
      <p class="how-step outlined">* YOU MUST BE OVER 16 TO USE THIS SERVICE.</p>
      <p class="how-step outlined">SEND A TEXT TO 64915 STARTING WITH Q4 THEN A SHORT NOTE ABOUT WHAT IS ON YOUR MIND.</p>
      <p class="how-step outlined">A QUALIFIED COUNSELLOR READS EVERY MESSAGE AND REPLIES WITH BRIEF, HONEST GUIDANCE.</p>
      <p class="how-step outlined">YOUR NUMBER IS NEVER SHARED AND ALL MESSAGES ARE KEPT PRIVATE.</p>
    </section>
    <div class="back-notes">
      <p>EACH REPLY COSTS £1.50 PLUS YOUR STANDARD NETWORK RATE.</p>
      <p>SERVICE RUN BY GAVINROWECOUNSELLING.UK</p>
      <p>TEXTS ARE ANSWERED WITHIN 24 HOURS, MONDAY TO FRIDAY.</p>
      <p>TO OPT OUT AT ANY TIME TEXT STOP TO 64915.</p>
    </div>
    <div class="share-row" aria-hidden="true">
      <span class="share-tile"></span><span class="share-tile"></span>
      <span class="share-tile"></span><span class="share-tile"></span>
    </div>
    <div class="figure" role="img" aria-label="Drawn illustration of the counsellor's shoulders and orange tie"></div>
  </article>

  <article class="flyer front">
    <h1 class="site-name outlined">CHATPAL.CO.UK</h1>
    <div class="registration">
      <p class="registration-label">REGISTERED WITH</p>
      <p class="registration-name">CALLTARIFFHUB</p>
    </div>
    <div class="figure" role="img" aria-label="Drawn illustration of a counsellor in a grey suit and orange tie, speaking"></div>
    <section class="speech-bubble">
      <p class="headline outlined">NEED FREE<br>CONFIDENTIAL<br>ADVICE?</p>
      <p class="topics outlined">WE HELP WITH:<br>WORK<br>HEALTH<br>RELATIONSHIPS<br>FAMILY ISSUES<br>&amp; MUCH MORE!</p>
      <p class="call-to-action outlined">JUST TEXT Q4<br>FOLLOWED BY<br>YOUR DILEMA<br>TO<br><span class="shortcode">64915</span></p>
      <p class="credentials outlined">WE ARE QUALIFIED COUNSELLORS WITH MANY YEARS EXPERIENCE OF DEALING WITH A VARIETY OF ISSUES FROM ADOLESCENTS TO ADULTS</p>
      <p class="pricing outlined">TEXTS COST £1.50 + THE STANDARD NETWORK FEE</p>
      <p class="terms outlined">OVER 16S ONLY<br>CHARGED PER TEXT</p>
    </section>
  </article>
</main>
</body>
</html>
```